Im open to ideas.. I was thinking on my business cards aswell as my logo. a place for my name. email. phone number and abn..

ive attched a file with my business logo. which i dont love the colours.. i was think a dark background with charcoal letters so something along those colour schumes but im open to ideas..

Business

BRL Constructions

```html
<!DOCTYPE html>
<html lang="en">
<head>
<meta charset="utf-8">
<title>BRL Constructions – Business Card</title>
<link href="https://fonts.googleapis.com/css2?family=Quicksand:wght@300;700&display=swap" rel="stylesheet">
<style>
  :root {
    --bg-centre: #2e3033;
    --bg-mid: #1f2022;
    --bg-edge: #111213;
    --charcoal-brand: #75797e;
    --charcoal-trade: #5f6368;
    --charcoal-text: #8d9196;
    --charcoal-line: #5f6368;
  }
  html, body {
    margin: 0;
    padding: 0;
    width: 1200px;
    height: 1200px;
    overflow: hidden;
    background: var(--bg-edge);
  }
  .card {
    position: relative;
    width: 1200px;
    height: 1200px;
    overflow: hidden;
    font-family: "Quicksand", sans-serif;
  }
  .card-texture {
    position: absolute;
    inset: 0;
    background: radial-gradient(ellipse at 50% 45%, var(--bg-centre) 0%, var(--bg-mid) 60%, var(--bg-edge) 100%);
  }
  .brand {
    position: absolute;
    left: 0;
    right: 0;
    margin: 0;
    text-align: center;
    font-weight: 700;
    line-height: 1;
  }
  .brand-name {
    top: 50px;
    font-size: 270px;
    letter-spacing: 0.28em;
    padding-left: 0.28em;
    color: var(--charcoal-brand);
  }
  .brand-trade {
    top: 300px;
    font-size: 92px;
    letter-spacing: 0.02em;
    color: var(--charcoal-trade);
  }
  .accent-line {
    position: absolute;
    left: 1030px;
    top: 316px;
    width: 8px;
    height: 740px;
  }
  .contact {
    position: absolute;
    left: 0;
    right: 0;
    margin: 0;
    text-align: center;
    color: var(--charcoal-text);
    font-weight: 300;
    font-size: 60px;
    line-height: 1;
    letter-spacing: 1.05em;
    padding-left: 1.05em;
  }
  .contact-name  { top: 450px; }
  .contact-phone { top: 615px; }
  .contact-email { top: 780px; }
  .contact-abn   { top: 945px; }
</style>
</head>
<body>
  <main class="card">
    <div class="card-texture" role="img" aria-label="Dark charcoal low-poly faceted background texture"></div>

    <h1 class="brand brand-name">BRL</h1>
    <p class="brand brand-trade">CONSTRUCTIONS</p>

    <svg class="accent-line" viewBox="0 0 8 740" preserveAspectRatio="none" aria-hidden="true">
      <defs>
        <linearGradient id="lineFade" x1="0" y1="0" x2="0" y2="1">
          <stop offset="0" stop-color="#5f6368"/>
          <stop offset="0.7" stop-color="#5f6368"/>
          <stop offset="1" stop-color="#5f6368" stop-opacity="0"/>
        </linearGradient>
      </defs>
      <polygon points="0,0 8,50 8,740 0,740" fill="url(#lineFade)"/>
    </svg>

    <p class="contact contact-name">NAME</p>
    <p class="contact contact-phone">PHONE</p>
    <p class="contact contact-email">EMAIL</p>
    <p class="contact contact-abn">ABN</p>
  </main>
</body>
</html>
```